Clean and modern business cards

Looking for an updated business card design for my dental office “corvanta dental” . Looking for a modern clean / sleek design . I’m thinking black background but open to seeing other options . One side needs to have an appointment card . Card needs to have logo, dentist name , phone, email , address . I’ve attached couple of cards I thought were cool as well as my logo
Target Market(s)
Dental patients
Industry/Entity Type
Dentistry
Contact Information for Business Card
Phone email address

```html
<!DOCTYPE html>
<html lang="en">
<head>
<meta charset="utf-8">
<title>Corvanta Dental – Business Cards</title>
<link href="https://fonts.googleapis.com/css2?family=Montserrat:wght@400;500;600&family=Oswald:wght@500&display=swap" rel="stylesheet">
<style>
  :root {
    --backdrop: #2a2a2c;
    --card-black: #1b1b1c;
    --card-paper: #e7e7e6;
    --ink: #2b2b2b;
    --ink-soft: #5a5a5a;
    --logo-silver: #d9d9d9;
    --accent-green: #9cbd2a;
    --band-purple: #5b1f9a;
    --band-blue: #2f4fa8;
    --band-red: #c8441f;
    --band-green: #9cbd2a;
    --band-sky: #5fa9c9;
    --contact-grey: #b9b9b9;
  }
  * { box-sizing: border-box; margin: 0; padding: 0; }
  html, body { width: 1200px; height: 868px; overflow: hidden; }
  body {
    background: var(--backdrop);
    font-family: "Montserrat", Arial, sans-serif;
    display: flex;
    align-items: center;
    justify-content: center;
    gap: 60px;
  }
  .card {
    width: 500px;
    height: 286px;
    background: var(--card-black);
    position: relative;
    overflow: hidden;
    box-shadow: 0 18px 40px rgba(0,0,0,.45);
  }

  /* Appointment side */
  .appointment-card .brand {
    position: absolute;
    top: 34px;
    left: 0;
    right: 0;
    display: flex;
    align-items: center;
    justify-content: center;
    gap: 14px;
  }
  .brand-dot {
    width: 44px; height: 44px;
    border-radius: 50%;
    background: var(--logo-silver);
  }
  .brand-name {
    font-weight: 600;
    font-size: 26px;
    letter-spacing: 2px;
    color: var(--logo-silver);
    text-transform: uppercase;
  }
  .colour-band {
    position: absolute;
    top: 110px; left: 0; right: 0;
    height: 5px;
    display: flex;
  }
  .colour-band span { flex: 1; }
  .colour-band .purple { background: var(--band-purple); }
  .colour-band .blue { background: var(--band-blue); }
  .colour-band .red { background: var(--band-red); }
  .colour-band .green { background: var(--band-green); }
  .colour-band .sky { background: var(--band-sky); }
  .appointment-form {
    position: absolute;
    top: 115px; left: 0; right: 0; bottom: 0;
    background: var(--card-paper);
    padding: 28px 34px 0;
    color: var(--ink);
  }
  .field-row { display: flex; align-items: flex-end; gap: 8px; margin-bottom: 20px; font-size: 13px; }
  .field-row .label { white-space: nowrap; }
  .field-row .line { flex: 1; border-bottom: 1px dotted var(--ink-soft); height: 1px; margin-bottom: 3px; }
  .field-row .suffix { font-size: 9px; font-weight: 500; }
  .cancel-note {
    font-size: 10px;
    line-height: 1.45;
    color: var(--ink-soft);
    text-align: center;
    margin-top: 4px;
  }

  /* Contact side */
  .emboss-mark {
    position: absolute;
    left: 40px; top: 60px;
    width: 250px; height: 210px;
    border-radius: 50%;
    background: radial-gradient(circle, #222223 0%, #1d1d1e 60%, var(--card-black) 100%);
  }
  .contact-block {
    position: absolute;
    top: 30px; right: 28px;
    text-align: right;
  }
  .dentist-name {
    font-family: "Oswald", "Arial Narrow", sans-serif;
    font-weight: 500;
    font-size: 19px;
    color: var(--accent-green);
    text-transform: uppercase;
    margin-bottom: 8px;
  }
  .contact-line {
    display: flex;
    justify-content: flex-end;
    align-items: center;
    gap: 8px;
    font-size: 9.5px;
    line-height: 1.55;
    color: var(--contact-grey);
  }
  .contact-line svg { width: 8px; height: 8px; fill: var(--accent-green); flex: none; }
  .contact-line .spacer { width: 8px; flex: none; }
</style>
</head>
<body>

<section class="card appointment-card">
  <div class="brand">
    <span class="brand-dot"></span>
    <span class="brand-name">Corvanta Dental</span>
  </div>
  <div class="colour-band">
    <span class="purple"></span><span class="blue"></span><span class="red"></span><span class="green"></span><span class="sky"></span>
  </div>
  <div class="appointment-form">
    <div class="field-row"><span class="label">Name:</span><span class="line"></span></div>
    <div class="field-row">
      <span class="label">Date:</span><span class="line"></span>
      <span class="label">Time:</span><span class="line"></span><span class="suffix">AM/PM</span>
    </div>
    <p class="cancel-note">To cancel or reschedule please notify us at least 48 hours<br>prior to your scheduled appointment</p>
  </div>
</section>

<section class="card contact-card">
  <div class="emboss-mark" role="img" aria-label="Blind-embossed brand symbol surrounded by bubbles"></div>
  <div class="contact-block">
    <h1 class="dentist-name">Dr. Elias Varnholt</h1>
    <div class="contact-line">
      <span>2410 Alder Creek Rd</span>
      <svg viewBox="0 0 10 10"><path d="M5 0a3.5 3.5 0 0 0-3.5 3.5C1.5 6 5 10 5 10s3.5-4 3.5-6.5A3.5 3.5 0 0 0 5 0zm0 5a1.4 1.4 0 1 1 0-2.8A1.4 1.4 0 0 1 5 5z"/></svg>
    </div>
    <div class="contact-line"><span>Winnipeg, MB</span><span class="spacer"></span></div>
    <div class="contact-line">
      <span>204.555.0142</span>
      <svg viewBox="0 0 10 10"><path d="M2 0l2 2.5-1.2 1.2a6 6 0 0 0 3.5 3.5L7.5 6 10 8l-1.5 2C4 10 0 6 0 1.5z"/></svg>
    </div>
    <div class="contact-line">
      <span>204.555.0187</span>
      <svg viewBox="0 0 10 10"><rect x="2" y="0" width="6" height="3"/><rect x="0" y="3.5" width="10" height="4.5" rx="1"/><rect x="2" y="7" width="6" height="3"/></svg>
    </div>
    <div class="contact-line">
      <span>hello@corvantadental.ca</span>
      <svg viewBox="0 0 10 10"><path d="M0 2h10v6H0z M0 2l5 3.5L10 2" fill="none" stroke="#9cbd2a" stroke-width="1.2"/></svg>
    </div>
    <div class="contact-line">
      <span>www.corvantadental.ca</span>
      <svg viewBox="0 0 10 10"><circle cx="5" cy="5" r="4.3" fill="none" stroke="#9cbd2a" stroke-width="1.2"/><path d="M0.7 5h8.6M5 0.7c-2.5 2.8-2.5 5.8 0 8.6M5 0.7c2.5 2.8 2.5 5.8 0 8.6" fill="none" stroke="#9cbd2a" stroke-width=".8"/></svg>
    </div>
  </div>
</section>

</body>
</html>
```